Baseball Coaching Camp for 5-14year olds needs sales campaign

Local baseball coaching camp for children is in it's 22nd year running a 4-5 week series of summer camps. Each year we use email marketing beginning around December to sell our camps to the parents to sign up their children for one or more weeks. All information about the camps can be seen on our website at https://quernhill.net/. In the past we have had success by changing the look of the emails each month and offering a decreasing discount as the camps get closer.

Our target market is the parents of children ages 5-14years old who like and play baseball and are interested in improving their skills in a fun environment during the Summer months.

We would like to improve the sales by developing new creative and imaginative emails for this season. We need 6 to 8 quality ads that can somehow relate to each other , these ads will be sent via our mailing list as well as used on social media. One of the owners thought it would be nice to use the "lantern harbor" theme though we are open to all ideas.
We have given you access to a dropbox link with examples of past campaigns along with artwork and images here
https://www.filecrate.example/sh/q7tmwpz2kdrlvha/BBKfe-moWenaXr7QuLP815cXo?dl=0

```html
<!DOCTYPE html>
<html lang="en">
<head>
<meta charset="utf-8">
<title>Quernhill Baseball Academy – Summer Camps</title>
<link href="https://fonts.googleapis.com/css2?family=Open+Sans:wght@400;600;700&family=Roboto:wght@400;500;700;900&display=swap" rel="stylesheet">
<style>
  :root {
    --brand: #3e4f9e;
    --ink: #222222;
    --body: #333333;
    --white: #ffffff;
    --footer-bg: #f5f5f5;
    --field-line: #555555;
  }
  * { margin: 0; padding: 0; box-sizing: border-box; }
  html, body { width: 1200px; height: 3836px; overflow: hidden; }
  body { position: relative; background: var(--white); font-family: "Open Sans", sans-serif; color: var(--body); }
  .abs { position: absolute; }

  .wordmark { font-family: "Roboto", sans-serif; font-weight: 700; color: var(--brand); font-size: 56px; line-height: 100px; letter-spacing: 2px; }
  .header-logo { left: 75px; top: 26px; height: 100px; }
  .header-phone { right: 80px; top: 44px; font-family: "Roboto", sans-serif; font-weight: 700; font-size: 50px; color: var(--brand); letter-spacing: 1px; }

  .hero { left: 0; top: 155px; width: 1200px; height: 787px;
    background: linear-gradient(135deg, #4a5240 0%, #6b5a44 40%, #8a7258 65%, #5e4a3a 100%); }
  .hero-title { left: 75px; top: 270px; width: 540px; font-family: "Open Sans", sans-serif; font-size: 74px; line-height: 110px; color: var(--white); font-weight: 400; }

  .season-banner { left: 75px; top: 890px; width: 1050px; height: 131px; background: var(--brand); border-radius: 22px;
    display: flex; align-items: center; justify-content: center; color: var(--white); font-family: "Roboto", sans-serif; font-weight: 400; font-size: 47px; letter-spacing: 0.5px; }

  .discount-art { left: 80px; top: 1075px; width: 500px; height: 355px;
    background: linear-gradient(180deg, #e8473f 0%, #c7242a 100%); border-radius: 4px; }
  .theme-title { left: 588px; top: 1080px; font-family: "Roboto", sans-serif; font-weight: 400; font-size: 46px; color: var(--brand); letter-spacing: 1px; }
  .theme-text { left: 591px; top: 1162px; width: 530px; font-size: 22px; line-height: 52px; color: var(--body); }

  .objectives-band { left: 0; top: 1512px; width: 1200px; height: 596px; background: var(--brand); }
  .objectives-title { left: 0; top: 1590px; width: 1200px; text-align: center; font-family: "Roboto", sans-serif; font-weight: 400; font-size: 47px; color: var(--white); }
  .objectives-text { left: 115px; top: 1670px; width: 970px; text-align: center; font-size: 22px; line-height: 45px; color: var(--white); }
  .team-photo { left: 75px; top: 1905px; width: 1050px; height: 488px;
    background: linear-gradient(180deg, #5f8a4a 0%, #3f6a33 45%, #d8b838 62%, #d9b83a 78%, #5d8a45 100%); }

  .mailing-title { left: 0; top: 2465px; width: 1200px; text-align: center; font-family: "Roboto", sans-serif; font-weight: 400; font-size: 47px; color: var(--brand); letter-spacing: 1px; }
  .field { left: 260px; width: 682px; height: 79px; border: 2px solid var(--field-line); display: flex; align-items: center; padding-left: 27px; font-size: 23px; color: #666666; }
  .field-name { top: 2565px; }
  .field-email { top: 2670px; }
  .field-phone { top: 2775px; }
  .submit { left: 260px; top: 2877px; width: 682px; height: 79px; background: var(--brand); color: var(--white);
    display: flex; align-items: center; justify-content: center; font-family: "Roboto", sans-serif; font-weight: 700; font-size: 26px; letter-spacing: 1px; }

  .contact { left: 0; top: 3108px; width: 1200px; height: 552px; background: var(--footer-bg); }
  .footer-logo { left: 0; top: 3192px; width: 1200px; height: 100px; text-align: center; }
  .contact-title { left: 0; top: 3330px; width: 1200px; text-align: center; font-family: "Roboto", sans-serif; font-weight: 700; font-size: 48px; color: var(--ink); letter-spacing: 1px; }
  .contact-line { left: 0; width: 1200px; text-align: center; font-size: 25px; color: var(--ink); letter-spacing: 0.5px; }
  .cl-1 { top: 3403px; } .cl-2 { top: 3455px; } .cl-3 { top: 3508px; } .cl-4 { top: 3560px; }

  .bottom-bar { left: 0; top: 3660px; width: 1200px; height: 176px; background: var(--brand); }
  .social { top: 3699px; width: 61px; height: 61px; border-radius: 50%; background: var(--white); }
  .social-a { left: 532px; } .social-b { left: 606px; }
  .copyright { left: 0; top: 3776px; width: 1200px; text-align: center; font-size: 21px; color: var(--white); letter-spacing: 0.5px; }
</style>
</head>
<body>
  <header>
    <div class="abs wordmark header-logo">Quernhill</div>
    <div class="abs header-phone">(555) 014-2290</div>
  </header>

  <section>
    <div class="abs hero" role="img" aria-label="Photo of a young batter in a yellow jersey swinging at a pitch with the catcher behind him on a baseball field"></div>
    <h1 class="abs hero-title">Local baseball coaching camp for children is in it's 22nd year running</h1>
    <div class="abs season-banner">A 4-5 WEEK SERIES OF SUMMER CAMPS</div>
  </section>

  <section>
    <div class="abs discount-art" role="img" aria-label="Large red three-dimensional 50% off graphic"></div>
    <h2 class="abs theme-title">LANTERN HARBOR</h2>
    <p class="abs theme-text">Our target market is the parents of children ages 5-14years old who like and play baseball and are interested in improving their skills in a fun environment during the Summer months.</p>
  </section>

  <section>
    <div class="abs objectives-band"></div>
    <h2 class="abs objectives-title">CAMP OBJECTIVES</h2>
    <p class="abs objectives-text">QUERNHILL BASEBALL CAMP provides a safe, fun, and educational environment where both beginner, as well as experienced players can excel. Throughout the week, your child will learn the basic fundamentals of the game and be able to specialize in the position of their choice. Each camper will learn the importance of team work, sportsmanship, and fair play.</p>
    <div class="abs team-photo" role="img" aria-label="Group photo of campers in yellow shirts and coaches in blue on a grass field in front of trees"></div>
  </section>

  <section>
    <h2 class="abs mailing-title">JOIN OUR MAILING LIST</h2>
    <div class="abs field field-name">Full Name</div>
    <div class="abs field field-email">Email Address</div>
    <div class="abs field field-phone">Phone Number</div>
    <div class="abs submit">SUBMIT</div>
  </section>

  <footer>
    <div class="abs contact"></div>
    <div class="abs wordmark footer-logo">Quernhill</div>
    <h2 class="abs contact-title">CONTACT US</h2>
    <p class="abs contact-line cl-1">QUERNHILL BASEBALL ACADEMY</p>
    <p class="abs contact-line cl-2">(555) 014-2290</p>
    <p class="abs contact-line cl-3">info@quernhill.net</p>
    <p class="abs contact-line cl-4">PO Box 48 Ashford Bay, New York 10990–0012</p>
    <div class="abs bottom-bar"></div>
    <div class="abs social social-a" role="img" aria-label="Social link"></div>
    <div class="abs social social-b" role="img" aria-label="Social link"></div>
    <p class="abs copyright">© 2021 QUERNHILL BASEBALL ACADEMY</p>
  </footer>
</body>
</html>
```